Stationary Design
Wexley Money Services
To all designer:
Thanks for submitting the revision and they are looking great. Here are some small minor adjustment on my information:
1) Envelope: Just need my mailing address
2) Folder: Just need my mailing address and Web address
3) Letterhead: Just need my phone number, mailing address and web address.
I made a mistake previously on my logo design project not finalizing the details and end up wasting a lot of time.
I appreciate everyone's patient on this.
To all designer: Just a friendly reminder:
Business Card: Please remove my license number.
Lettheads: No need to include my email and cell number.
Envelope: Just need to include website address and mailing address.
Thanks!!
pelicanjot (#29)
Really nice business card. Is the watermark suppose to cover front and back? It is possible you can make it all fit on the front side? Can you shrink the font size for my name and title as well as the logo on the backside of card?
qirrr (#25,#26)
Thanks for designing the whole set as well. This is a very creative design and I've been starting at it for at least 20 minutes trying to visualize printing this on a regular folder/card/letterhead..etc. I think the wave/green shape might need to be shrink down on the folders and business card. It maybe a bit overpowering.
Velustro (#18, #19)
Thank you for designing the whole set. I really appreciated. For the business card, if you can shrink the watermark logo on the back side, would look really nice. For the folder, I would prefer to see less of the green and black color. The folder would actually work for me if you even make the front shape smaller and backside white color with watermark of the logo.
Plenmorix (#17)
Thanks for providing few variations for the design.
I like the second letterhead but maybe we can look at using the watermark in the middle instead of the logo on the bottom. For the business card, the last one is nice. I would prefer to see them smaller size (logo and fonts) and possibly use watermark for the shape instead of solid green.
Tarn47 (#6, #22)
I like the layout of #6. If possible, we can look at grey/white background on the backside and maybe shrinking the logo down a bit on the front side. #22's business card is nice as well. I think grey/white backside will look really nice. I liked the placement of information for the envelope and letterhead. The watermark is a nice touch. Is it possible to look at possibly reducing the logo down a bit? I'm curious to see what it looks like.
owlcrafts (#2)
I liked the business card a lot, especially the backside. For the letterhead, as per my comment to everyone, maybe shrinking my contact information down more. Not sure if you can incorporate some grey watermark of the logo into the letterhead.
Envelope i really liked as well. Especially the backside. For the front, is it possible to shrink the logo down a bit and lower it? I won't be using the window envelope.
For the folder, I think it has too much of either green or grey. Is it possible to utilize less color and more watermark/white background?
Hi all, thanks for the additional submission and revision. I really do appreciated. I've decided to eliminate a few designs and keep the best ones from each of designer. This will clear up some space.
To all Designers:
Business card: Please remove license number and less green in general.
Letterhead: Pleas remove my email and i would like the contact information as less visible as possible. So maybe try smaller size font or placing it on bottom or side of the sheet.
Folders: Doesn't have to be too much color usage. It can be simple.
Envelope: Can be simple as well. I actually liked most of designers' envelope. Each has it's own unique style.
Updated. Thanks!
For letterheads and envelope. You don't have to include all the information. Just need:
1) address
2) phone, fax and toll free (do not need my cell)
You don't have to include my Lic#/cell phone.
Thanks.
Thanks for the prompt submission everyone. I just designed this logo last week and the color green is fairly new to me. I think if possible, to use less Green and more of the grey and white. That may help to bring up the green more. For example, like #2 and #5. Really nice usage of the grey on the back of the card.
For the layout of the content (biz card), i like the information placement on #2, #4, #6 and #16. The information are aligned and my name is clearly recognize without overpowering the rest of the information.

```html
<!DOCTYPE html>
<html lang="en">
<head>
<meta charset="utf-8">
<title>Wexley Money Services — Stationery Set</title>
<link href="https://fonts.googleapis.com/css2?family=Questrial&display=swap" rel="stylesheet">
<style>
  :root {
    --stage: #000000;
    --paper: #ffffff;
    --brand-green: #8cb63c;
    --brand-grey: #6b6c6f;
    --flap-grey: #5f6062;
    --card-grey: #6e6f72;
    --watermark: #eef3e4;
    --watermark-grey: #f1f1f1;
    --ink-soft: #8a8b8d;
  }
  * { margin: 0; padding: 0; box-sizing: border-box; }
  html, body { width: 1200px; height: 569px; overflow: hidden; background: var(--stage); }
  body { font-family: "Questrial", sans-serif; position: relative; }

  .sheet { position: absolute; background: var(--paper); overflow: hidden; }

  .watermark {
    position: absolute; border-radius: 50%;
    background: radial-gradient(circle at 40% 40%, var(--watermark) 0%, var(--watermark-grey) 70%, transparent 71%);
  }

  .brand { position: absolute; display: flex; align-items: center; gap: 6px; color: var(--brand-grey); white-space: nowrap; }
  .brand-dot { border-radius: 50%; background: var(--brand-green); flex: none; }
  .brand-name { line-height: 1; }

  .contact { position: absolute; color: var(--ink-soft); font-size: 5px; line-height: 7px; white-space: nowrap; }
  .contact .line { display: block; }

  /* business cards */
  .card { top: 77px; width: 137px; height: 81px; }
  .card--front { left: 367px; }
  .card--back { left: 516px; background: var(--card-grey); }
  .card--info { left: 667px; }
  .card .person { position: absolute; left: 8px; top: 8px; font-size: 5px; line-height: 7px; color: var(--brand-grey); }
  .card .person strong { font-weight: 400; color: var(--brand-green); font-size: 6px; }
  .card--front .brand { right: 8px; top: 9px; flex-direction: column; align-items: center; gap: 2px; }

  /* envelopes */
  .envelope { width: 379px; height: 183px; }
  .envelope--back-left { left: 29px; top: 168px; }
  .envelope--back-right { left: 425px; top: 168px; }
  .envelope--front-left { left: 29px; top: 365px; }
  .envelope--front-right { left: 425px; top: 365px; }
  .flap { position: absolute; left: 0; top: 0; width: 100%; height: 34px; background: var(--flap-grey); }
  .flap-edge { position: absolute; left: 0; top: 34px; width: 100%; height: 3px; background: linear-gradient(#d9d9d9, var(--paper)); }

  /* letterhead */
  .letterhead { left: 845px; top: 77px; width: 331px; height: 470px; }
</style>
</head>
<body>

  <!-- business card: front -->
  <section class="sheet card card--front" aria-label="Business card front">
    <div class="watermark" style="left:70px;top:-10px;width:90px;height:90px;"></div>
    <p class="person"><strong>Alan Reyes</strong><br>Loan Officer<br>T 555 201 4410<br>wexleymoney.com</p>
    <div class="brand">
      <span class="brand-dot" style="width:9px;height:9px;"></span>
      <span class="brand-name" style="font-size:6px;">Wexley Money Services</span>
    </div>
  </section>

  <!-- business card: back -->
  <section class="sheet card card--back" aria-label="Business card back">
    <div class="brand" style="left:22px;top:33px;gap:4px;color:var(--paper);">
      <span class="brand-dot" style="width:12px;height:12px;background:var(--paper);"></span>
      <span class="brand-name" style="font-size:8px;">Wexley Money Services</span>
    </div>
  </section>

  <!-- business card: info side -->
  <section class="sheet card card--info" aria-label="Business card information side">
    <div class="watermark" style="left:78px;top:-8px;width:80px;height:80px;"></div>
    <p class="person"><strong>Alan Reyes</strong><br>Loan Officer<br>1820 Harbor Lane<br>Fairmont, CA 94010</p>
  </section>

  <!-- envelope backs -->
  <section class="sheet envelope envelope--back-left" aria-label="Envelope back">
    <div class="flap"></div><div class="flap-edge"></div>
    <div class="brand" style="left:138px;top:10px;gap:5px;color:var(--paper);">
      <span class="brand-dot" style="width:14px;height:14px;background:var(--paper);"></span>
      <span class="brand-name" style="font-size:8px;">Wexley Money Services</span>
    </div>
  </section>

  <section class="sheet envelope envelope--back-right" aria-label="Envelope back">
    <div class="flap"></div><div class="flap-edge"></div>
    <div class="brand" style="left:130px;top:10px;gap:5px;color:var(--paper);">
      <span class="brand-dot" style="width:14px;height:14px;background:var(--paper);"></span>
      <span class="brand-name" style="font-size:9px;">Wexley Money Services</span>
    </div>
  </section>

  <!-- envelope fronts -->
  <section class="sheet envelope envelope--front-left" aria-label="Envelope front">
    <div class="watermark" style="left:255px;top:-20px;width:150px;height:150px;"></div>
    <div class="watermark" style="left:-30px;top:140px;width:90px;height:90px;"></div>
    <div class="brand" style="left:12px;top:24px;flex-direction:column;align-items:flex-start;gap:4px;">
      <span class="brand-dot" style="width:20px;height:20px;margin-left:10px;"></span>
      <span class="brand-name" style="font-size:12px;">Wexley Money Services</span>
    </div>
    <p class="contact" style="left:247px;top:138px;">
      <span class="line">1820 Harbor Lane, Suite 4</span>
      <span class="line">Fairmont, CA 94010</span>
      <span class="line">wexleymoney.com</span>
    </p>
  </section>

  <section class="sheet envelope envelope--front-right" aria-label="Envelope front">
    <div class="watermark" style="left:-20px;top:60px;width:140px;height:140px;"></div>
    <div class="brand" style="left:230px;top:24px;flex-direction:column;align-items:flex-end;gap:4px;">
      <span class="brand-dot" style="width:20px;height:20px;margin-right:40px;"></span>
      <span class="brand-name" style="font-size:12px;">Wexley Money Services</span>
    </div>
    <p class="contact" style="left:17px;top:138px;">
      <span class="line">1820 Harbor Lane, Suite 4</span>
      <span class="line">Fairmont, CA 94010</span>
      <span class="line">wexleymoney.com</span>
    </p>
  </section>

  <!-- letterhead -->
  <section class="sheet letterhead" aria-label="Letterhead">
    <div class="watermark" style="left:-50px;top:360px;width:150px;height:150px;"></div>
    <div class="brand" style="left:218px;top:12px;flex-direction:column;align-items:flex-end;gap:3px;">
      <span class="brand-dot" style="width:14px;height:14px;margin-right:30px;"></span>
      <span class="brand-name" style="font-size:8px;">Wexley Money Services</span>
    </div>
    <p class="contact" style="left:20px;top:440px;">
      <span class="line">T 555 201 4410 F 555 201 4411</span>
      <span class="line">1820 Harbor Lane, Suite 4, Fairmont, CA 94010</span>
      <span class="line">wexleymoney.com</span>
    </p>
  </section>

</body>
</html>
```